"Client Services Packet" Folder design for Hair Tissue Mineral Analysis Company

We are looking for an updated folder design which we use mail our new clients information and starter kits for our services. We are looking for a clean and simple design to match our new logo. We would like our logo along with "Client Services Packet" on the front cover with our company information located inside the folder.
Logo file and color palette will be uploaded in the brief.
**Folder will not need the business card cutout shown on current folder**
Address:
4718 E. Corbin Street
Tolvane, NV 89417
Phone:
1-602-418-7362
1-800-736-2915
Fax:
1-602-549-2096
Website:
www.vexmorlab.com
Email:
information@vexmorlab.com
Look and feel
Each slider illustrates characteristics of the customer's brand and the style your logo design should communicate.

```html
<!DOCTYPE html>
<html lang="en">
<head>
<meta charset="utf-8">
<title>Client Services Packet – Folder</title>
<link rel="stylesheet" href="https://fonts.googleapis.com/css2?family=Saira+Semi+Condensed:wght@500;600&family=Roboto:wght@400&display=swap">
<style>
  :root {
    --page-bg: #ffffff;
    --navy-deep: #15214a;
    --blue-mid: #2c4f9c;
    --blue-sheen: #6a8bcd;
    --blue-low: #2a4e9f;
    --type-light: #ffffff;
    --type-soft: #cfdaf2;
    --fold-line: #c9d4ee;
  }
  html, body {
    margin: 0;
    padding: 0;
    width: 806px;
    height: 1200px;
    overflow: hidden;
    background: var(--page-bg);
  }
  .canvas {
    position: relative;
    width: 806px;
    height: 1200px;
  }
  .folder-dieline {
    position: absolute;
    left: 34px;
    top: 300px;
    width: 738px;
    height: 601px;
  }
  .cover-title {
    font-family: "Saira Semi Condensed", sans-serif;
    font-weight: 600;
    font-size: 9px;
    letter-spacing: 0.4px;
    fill: var(--type-light);
  }
  .brand-name {
    font-family: "Saira Semi Condensed", sans-serif;
    font-weight: 600;
    font-size: 6.4px;
    letter-spacing: 0.5px;
    fill: var(--type-light);
  }
  .contact-line {
    font-family: "Roboto", sans-serif;
    font-weight: 400;
    font-size: 4px;
    fill: var(--type-soft);
  }
  .fold-line {
    stroke: var(--fold-line);
    stroke-width: 0.7;
    stroke-dasharray: 3 2.5;
    fill: none;
  }
</style>
</head>
<body>
<main class="canvas">
  <svg class="folder-dieline" viewBox="0 0 547 445" role="group" aria-label="Flat folder dieline: cover, side flaps and inside pocket">
    <defs>
      <linearGradient id="folder-blue" gradientUnits="userSpaceOnUse" x1="0" y1="0" x2="70" y2="445">
        <stop offset="0" stop-color="var(--navy-deep)"/>
        <stop offset="0.42" stop-color="var(--blue-mid)"/>
        <stop offset="0.53" stop-color="var(--blue-sheen)"/>
        <stop offset="0.62" stop-color="var(--blue-mid)"/>
        <stop offset="1" stop-color="var(--blue-low)"/>
      </linearGradient>
    </defs>

    <path class="cover-panel" d="M27 3 Q27 0 30 0 H514 Q517 0 517 3 V323 H27 Z" fill="url(#folder-blue)"/>

    <path class="side-flap" d="M0 226 L27 217 V323 L0 314 Z" fill="url(#folder-blue)"/>
    <path class="side-flap" d="M517 217 L547 226 V314 L517 323 Z" fill="url(#folder-blue)"/>

    <path class="pocket-panel" d="M27 323 H517 V445 H285 L270 323 L259 445 H27 Z" fill="url(#folder-blue)"/>

    <line class="fold-line" x1="0" y1="323" x2="547" y2="323"/>
    <line class="fold-line" x1="27" y1="217" x2="27" y2="323"/>
    <line class="fold-line" x1="517" y1="217" x2="517" y2="323"/>

    <text class="brand-name" x="410" y="40" text-anchor="middle">VEXMOR MINERAL GROUP</text>
    <text class="cover-title" x="382" y="99" text-anchor="middle">CLIENT SERVICES</text>
    <text class="cover-title" x="382" y="110" text-anchor="middle">PACKET</text>

    <g class="pocket-contact" transform="rotate(180 210 389)">
      <text class="brand-name" x="166" y="370">VEXMOR MINERAL GROUP</text>
      <text class="contact-line" x="166" y="380">4718 E. Corbin Street • Tolvane, NV 89417</text>
      <text class="contact-line" x="166" y="386">Phone: 1-602-418-7362 • 1-800-736-2915 • Fax: 1-602-549-2096</text>
      <text class="contact-line" x="166" y="392">Website: www.vexmorlab.com • Email: information@vexmorlab.com</text>
    </g>
  </svg>
</main>
</body>
</html>
```